Brasko Construction Business Card

I need a business card design for my company.
We are a construction/machinery company.
I would like to see my logo on the front of the card and my details on the other side
I would like the card to be black or dark grey in colour,with my logo as i send it or modified with a lighter blue colour
I would like to see the design kept fairly simple,but eye catching at the same time
Industry/Entity Type
Business
Contact Information for Business Card
Name
Phone Number
Address
Email
Colors
00a990
1b1b1b
000000
474747
ececec

```html
<!DOCTYPE html>
<html lang="en">
<head>
<meta charset="utf-8">
<title>Brasko Construction Business Card</title>
<link rel="stylesheet" href="https://fonts.googleapis.com/css2?family=Open+Sans:wght@400;700&display=swap">
<style>
  :root {
    --backdrop: #3a3a3a;
    --card: #1f1f1f;
    --ink: #ececec;
    --rule: #8a8a8a;
    --icon-glyph: #1b1b1b;
  }
  * { margin: 0; padding: 0; box-sizing: border-box; }
  html, body {
    width: 1200px;
    height: 1189px;
    overflow: hidden;
    background: var(--backdrop);
    font-family: "Open Sans", sans-serif;
    color: var(--ink);
  }
  .stage {
    position: relative;
    width: 1200px;
    height: 1189px;
  }
  .card {
    position: absolute;
    left: 220px;
    width: 760px;
    height: 434px;
    background: var(--card);
    border-radius: 26px;
    box-shadow: 0 14px 30px rgba(0,0,0,0.45);
  }
  .card--front { top: 120px; }
  .card--back { top: 630px; }

  .wordmark {
    display: flex;
    align-items: center;
    gap: 16px;
    font-weight: 700;
    text-transform: uppercase;
    color: var(--ink);
    line-height: 1.05;
  }
  .wordmark__square {
    width: 54px;
    height: 54px;
    background: var(--ink);
    flex: none;
  }
  .wordmark__name { display: flex; flex-direction: column; }
  .wordmark__line1 { font-size: 62px; letter-spacing: 2px; }
  .wordmark__line2 { font-size: 30px; letter-spacing: 6px; }

  .card--front .wordmark {
    position: absolute;
    left: 50%;
    top: 50%;
    transform: translate(-50%, -50%);
  }

  .card--back .wordmark {
    position: absolute;
    left: 56px;
    top: 50%;
    transform: translateY(-50%);
  }
  .card--back .wordmark__square { width: 40px; height: 40px; }
  .card--back .wordmark__line1 { font-size: 46px; }
  .card--back .wordmark__line2 { font-size: 22px; letter-spacing: 4px; }

  .divider {
    position: absolute;
    left: 405px;
    top: 110px;
    width: 1px;
    height: 214px;
    background: var(--rule);
  }
  .contact {
    position: absolute;
    left: 440px;
    top: 110px;
    font-size: 19px;
    line-height: 1.4;
  }
  .contact__name {
    font-size: 24px;
    font-weight: 700;
    margin-bottom: 22px;
  }
  .contact__address { margin-bottom: 4px; }
  .contact__row {
    display: flex;
    align-items: center;
    gap: 10px;
    margin-top: 4px;
  }
  .contact__icon {
    width: 24px;
    height: 24px;
    flex: none;
  }
</style>
</head>
<body>
<main class="stage">
  <section class="card card--front" aria-label="Card front">
    <div class="wordmark">
      <span class="wordmark__square"></span>
      <span class="wordmark__name">
        <span class="wordmark__line1">Brasko</span>
        <span class="wordmark__line2">Construction</span>
      </span>
    </div>
  </section>

  <section class="card card--back" aria-label="Card back">
    <div class="wordmark">
      <span class="wordmark__square"></span>
      <span class="wordmark__name">
        <span class="wordmark__line1">Brasko</span>
        <span class="wordmark__line2">Construction</span>
      </span>
    </div>
    <div class="divider"></div>
    <div class="contact">
      <p class="contact__name">Employee Name</p>
      <p class="contact__address">P.O. Box 000, 2nd Street<br>Millbrook, USA</p>
      <p class="contact__row">
        <svg class="contact__icon" viewBox="0 0 24 24" aria-hidden="true">
          <rect width="24" height="24" rx="5" fill="var(--ink)"/>
          <path d="M8 5.5c.6 0 1.2.4 1.4 1l.8 2.2c.2.5 0 1-.4 1.3l-1 .8c.8 1.7 2 2.9 3.6 3.7l.8-1c.3-.4.9-.6 1.3-.4l2.2.8c.6.2 1 .8 1 1.4v1.5c0 .8-.7 1.4-1.5 1.4C10.4 19.2 4.8 13.6 4.8 7c0-.8.6-1.5 1.4-1.5z" fill="var(--icon-glyph)"/>
        </svg>
        <span>0123 456 000</span>
      </p>
      <p class="contact__row">
        <svg class="contact__icon" viewBox="0 0 24 24" aria-hidden="true">
          <rect width="24" height="24" rx="5" fill="var(--ink)"/>
          <rect x="5" y="7" width="14" height="10" fill="none" stroke="var(--icon-glyph)" stroke-width="1.6"/>
          <path d="M5 7l7 6 7-6" fill="none" stroke="var(--icon-glyph)" stroke-width="1.6"/>
        </svg>
        <span>info@braskobuild.com</span>
      </p>
    </div>
  </section>
</main>
</body>
</html>
```